Talvor GmbH business card

We Talvor GmbH based in Switzerland are looking for a business card design. The Fresh Jung, appealing to customers of all kinds. We already have a logo to upload but still a business card. Details: Talvor GmbH Address: Lindenweg 14b in 9476 Brugwil. Tel: 41 79 462 37 18, web: Talvor.ch, E-mail: info@Talvor.ch Facebook: Talvor GmbH. I am the Managing Director: Luka Petrovac. On reverse: Title: Transporter and bus rental Gross: Without deposit Super prices
Contact Information for Business Card
Siehe Projektbeschreibung
Requirements
Should not have
- Other pictures

```html
<!DOCTYPE html>
<html lang="de">
<head>
<meta charset="utf-8">
<title>Talvor GmbH – Visitenkarte</title>
<link href="https://fonts.googleapis.com/css2?family=Open+Sans:wght@400;600;700&display=swap" rel="stylesheet">
<style>
  :root {
    --navy: #1d1888;
    --navy-deep: #18147a;
    --white: #ffffff;
    --black: #050505;
    --backdrop: #e9e6e1;
    --card-w: 640px;
    --card-h: 366px;
  }
  * { box-sizing: border-box; margin: 0; padding: 0; }
  html, body {
    width: 1200px; height: 900px; overflow: hidden;
    background: var(--backdrop);
    font-family: "Open Sans", Arial, sans-serif;
  }
  .stage {
    width: 1200px; height: 900px;
    display: flex; flex-direction: column;
    align-items: center; justify-content: center; gap: 50px;
  }
  .card {
    width: var(--card-w); height: var(--card-h);
    position: relative; overflow: hidden;
    box-shadow: 0 6px 18px rgba(0,0,0,.18);
  }

  /* Front */
  .card-front {
    background: var(--navy);
    color: var(--white);
  }
  .card-front .texture {
    position: absolute; inset: 0;
    background: linear-gradient(135deg, var(--navy) 0%, var(--navy-deep) 100%);
  }
  .brand {
    display: flex; align-items: center; gap: 12px;
    font-weight: 700; font-size: 40px; letter-spacing: 1px;
    white-space: nowrap;
  }
  .brand-mark { width: 40px; height: 40px; background: currentColor; flex: none; }
  .card-front .brand {
    position: absolute; left: 128px; top: 120px;
  }
  .card-front .website {
    position: absolute; left: 0; right: 0; top: 232px;
    text-align: center; padding-left: 40px;
    font-size: 15px; font-weight: 600; letter-spacing: .3px;
  }

  /* Back */
  .card-back { background: var(--white); display: flex; flex-direction: column; }
  .back-logo {
    height: 52%;
    display: flex; align-items: center; justify-content: center;
    color: var(--navy);
    padding-top: 20px;
  }
  .contact-band {
    height: 27%; background: var(--navy); color: var(--white);
    display: flex; align-items: center; justify-content: center; gap: 14px;
    padding-left: 40px;
  }
  .person { text-align: right; }
  .person-name { font-size: 19px; font-weight: 700; line-height: 1.25; }
  .person-title { font-size: 15px; line-height: 1.25; }
  .divider { width: 1px; height: 42px; background: rgba(255,255,255,.6); }
  .contact-list { list-style: none; font-size: 14px; line-height: 1.55; }
  .contact-list li { display: flex; align-items: center; gap: 7px; }
  .contact-list svg { width: 12px; height: 12px; flex: none; }
  .icon-phone { fill: var(--white); }
  .icon-mail { fill: var(--white); }
  .address-band {
    flex: 1; background: var(--black); color: var(--white);
    display: flex; align-items: center; justify-content: center;
    font-size: 17px; letter-spacing: .3px;
  }
</style>
</head>
<body>
<main class="stage">
  <section class="card card-front" aria-label="Kartenvorderseite">
    <div class="texture" role="img" aria-label="Feines dunkelblaues Hintergrundmuster"></div>
    <div class="brand"><span class="brand-mark"></span>Talvor GmbH</div>
    <p class="website">www.Talvor.ch</p>
  </section>

  <section class="card card-back" aria-label="Kartenrückseite">
    <div class="back-logo">
      <div class="brand"><span class="brand-mark"></span>Talvor GmbH</div>
    </div>
    <div class="contact-band">
      <div class="person">
        <p class="person-name">Luka Petrovac</p>
        <p class="person-title">Managing Director</p>
      </div>
      <span class="divider"></span>
      <ul class="contact-list">
        <li>
          <svg class="icon-phone" viewBox="0 0 24 24" aria-hidden="true"><path d="M6.6 10.8a15.1 15.1 0 0 0 6.6 6.6l2.2-2.2a1 1 0 0 1 1-.25 11.4 11.4 0 0 0 3.6.57 1 1 0 0 1 1 1V20a1 1 0 0 1-1 1A17 17 0 0 1 3 4a1 1 0 0 1 1-1h3.5a1 1 0 0 1 1 1c0 1.25.2 2.45.57 3.57a1 1 0 0 1-.25 1z"/></svg>
          41 79 462 37 18
        </li>
        <li>
          <svg class="icon-mail" viewBox="0 0 24 24" aria-hidden="true"><path d="M2 5h20v2l-10 7L2 7z M2 9.4l10 7 10-7V19H2z"/></svg>
          info@Talvor.ch
        </li>
      </ul>
    </div>
    <div class="address-band">Lindenweg 14b, 9476 Brugwil, Switzerland</div>
  </section>
</main>
</body>
</html>
```